Lirelle Home Fragrance

I am looking to create a brand for my home fragrance line ( diffusers and candles). Looking for designs (logo) that will go on the diffuser bottle as well as the packaging for these.

Target Market(s)

online

Industry/Entity Type

Home Improvement

Font styles to use
Other font styles liked:
• Not sure what it's called, but something vintage. similar to the attached photo

Colors

Designer to choose colors to be used in the design.

Requirements
Must have
• Attractive packages

```html
<!DOCTYPE html>
<html lang="en">
<head>
<meta charset="utf-8">
<title>Lirelle Home Fragrance – Label</title>
<link rel="stylesheet" href="https://fonts.googleapis.com/css2?family=Cormorant+Garamond:wght@500;700&display=swap">
<style>
  :root {
    --stage: #e4e5e5;
    --stage-light: #f4f4f4;
    --ink: #000000;
    --paper: #ffffff;
    --panel-top: #b9b9b9;
    --panel-mid: #8e8e8e;
    --panel-low: #5a5a5a;
    --panel-base: #0c0c0c;
    --panel-edge: #6c6c6c;
    --text-dark: #0a0a0a;
    --text-light: #f2f2f2;
  }
  * { margin: 0; padding: 0; box-sizing: border-box; }
  html, body { width: 1200px; height: 853px; overflow: hidden; }
  body {
    background: linear-gradient(90deg, var(--stage) 0%, var(--stage-light) 100%);
    position: relative;
    font-family: "Cormorant Garamond", serif;
  }
  .label { position: absolute; left: 375px; top: 41px; width: 450px; height: 771px; }

  .tab {
    position: absolute; left: 131px; width: 188px;
    background: var(--ink);
  }
  .tab--top { top: 0; height: 133px; }
  .tab--bottom { top: 690px; height: 80px; border: 1px solid var(--paper); border-top: none; }
  .tab__window { position: absolute; left: 45px; width: 97px; background: var(--paper); }
  .tab--top .tab__window { top: 18px; height: 115px; }
  .tab--bottom .tab__window { top: 0; height: 61px; }

  .label__body {
    position: absolute; left: 0; top: 133px; width: 450px; height: 554px;
    background: var(--ink);
    border: 1px solid var(--paper);
  }
  .label__frame {
    position: absolute; inset: 11px;
    border: 2px solid var(--paper);
  }
  .label__panel {
    position: absolute; inset: 26px;
    border: 2px solid var(--panel-edge);
    background:
      radial-gradient(ellipse 70% 35% at 50% 22%, rgba(255,255,255,0.35), rgba(255,255,255,0) 70%),
      linear-gradient(180deg, var(--panel-top) 0%, var(--panel-mid) 45%, var(--panel-low) 78%, var(--panel-base) 100%);
  }
  .label__text { position: absolute; left: 0; width: 100%; text-align: center; }
  .brand-name {
    top: 105px;
    font-weight: 700; font-size: 78px; line-height: 1;
    letter-spacing: 4px; color: var(--text-dark);
  }
  .brand-descriptor {
    top: 186px;
    font-weight: 500; font-size: 36px; line-height: 1;
    color: var(--text-dark);
  }
  .scent-note {
    top: 405px;
    font-weight: 500; font-size: 26px; line-height: 31px;
    letter-spacing: 0.5px; color: var(--text-light);
  }
</style>
</head>
<body>
  <main class="label">
    <div class="tab tab--top"><div class="tab__window"></div></div>
    <section class="label__body">
      <div class="label__frame"></div>
      <div class="label__panel" role="img" aria-label="Silver-grey background of fine criss-crossing thread lines fading to black at the base">
        <h1 class="label__text brand-name">LIRELLE</h1>
        <p class="label__text brand-descriptor">Home Fragrance</p>
        <p class="label__text scent-note">Sandalwood and Amber scent<br>MADE WITH LOVE</p>
      </div>
    </section>
    <div class="tab tab--bottom"><div class="tab__window"></div></div>
  </main>
</body>
</html>
```